Company Racing Team Logo Sticker for print

For our company (Logo see file-area) we need some stickers for racing cars, trailers, equipment, ... It should include company logo as well as some adds (words, symbols, design elements,...) to make a connection to racing. Please try to create common design capable for different formatd (square, rectangle, longer rectangle, ...). Maybe an up to 3-digit number plate (16x16cm, 20x24cm), too? (I would like to be able to change the number in the future by myself) This number plate shoud use whole space for the number, also use background design witout ( or very, very small ) logo and/ or name.

Target Market(s)

Karting / Car Racing Public

Requirements
Must have
• logo

```html
<!DOCTYPE html>
<html lang="en">
<head>
<meta charset="utf-8">
<title>K-TRAX Race Number Plates</title>
<link rel="stylesheet" href="https://fonts.googleapis.com/css2?family=Archivo+Black&display=swap">
<style>
  :root {
    --ink: #000000;
    --sun: #f4e900;
    --paper: #ffffff;
    --brand-blue: #1c7fbf;
  }
  html, body {
    margin: 0;
    padding: 0;
    width: 1200px;
    height: 1024px;
    overflow: hidden;
    background: var(--paper);
  }
  .sheet { display: block; width: 1200px; height: 1024px; }
  .ink { fill: var(--ink); }
  .sun { fill: var(--sun); }
  .paper { fill: var(--paper); }
  .outline { stroke: var(--ink); stroke-width: 6; }
  .race-number {
    font-family: "Archivo Black", "Arial Black", sans-serif;
    font-size: 380px;
    text-anchor: middle;
  }
  .race-number.solid { fill: var(--ink); }
  .race-number.outlined {
    fill: var(--sun);
    stroke: var(--ink);
    stroke-width: 16;
    paint-order: stroke;
    stroke-linejoin: round;
  }
  .brand-name {
    font-family: "Archivo Black", "Arial Black", sans-serif;
    font-size: 44px;
    text-anchor: middle;
  }
  .brand-name.on-dark { fill: var(--paper); }
  .brand-name.on-sun { fill: var(--brand-blue); }
</style>
</head>
<body>
<svg class="sheet" viewBox="0 0 2048 1770" preserveAspectRatio="none" xmlns="http://www.w3.org/2000/svg">
  <defs>
    <!-- shared parts -->
    <g id="tread-strips">
      <rect class="ink" x="48" y="100" width="32" height="355" role="img" aria-label="Tyre tread strip"/>
      <rect class="ink" x="845" y="100" width="32" height="355" role="img" aria-label="Tyre tread strip"/>
    </g>
    <g id="mount-holes">
      <rect class="paper outline" x="248" y="38" width="62" height="30" rx="15"/>
      <rect class="paper outline" x="605" y="38" width="62" height="30" rx="15"/>
    </g>
  </defs>

  <!-- Row 1 left: yellow frame, black badge -->
  <g class="plate plate--sun-frame" transform="translate(75 47)">
    <rect class="sun outline" x="3" y="3" width="919" height="478" rx="30"/>
    <rect class="paper" x="78" y="100" width="769" height="355"/>
    <rect class="ink" x="3" y="100" width="48" height="370" rx="10"/>
    <rect class="ink" x="874" y="100" width="48" height="370" rx="10"/>
    <use href="#tread-strips"/>
    <rect class="paper outline" x="40" y="25" width="848" height="55" rx="14"/>
    <use href="#mount-holes"/>
    <text class="race-number solid" x="477" y="385" textLength="400" lengthAdjust="spacingAndGlyphs">29</text>
    <polygon class="ink" points="265,408 667,405 705,481 225,481"/>
    <text class="brand-name on-dark" x="470" y="463">K-TRAX</text>
  </g>

  <!-- Row 1 right: yellow frame, yellow badge -->
  <g class="plate plate--sun-frame" transform="translate(1050 47)">
    <rect class="sun outline" x="3" y="3" width="919" height="478" rx="30"/>
    <rect class="paper" x="78" y="100" width="769" height="355"/>
    <rect class="ink" x="3" y="100" width="48" height="370" rx="10"/>
    <rect class="ink" x="874" y="100" width="48" height="370" rx="10"/>
    <use href="#tread-strips"/>
    <rect class="paper outline" x="40" y="25" width="848" height="55" rx="14"/>
    <use href="#mount-holes"/>
    <text class="race-number solid" x="477" y="385" textLength="400" lengthAdjust="spacingAndGlyphs">29</text>
    <polygon class="sun" points="260,403 665,400 695,455 230,455"/>
    <text class="brand-name on-sun" x="462" y="455">K-TRAX</text>
  </g>

  <!-- Row 2 left: black frame, outlined yellow number -->
  <g class="plate plate--ink-frame" transform="translate(75 622)">
    <rect class="ink" x="0" y="0" width="925" height="484" rx="30"/>
    <rect class="sun" x="45" y="24" width="838" height="62" rx="12"/>
    <use href="#mount-holes" transform="translate(0 15)"/>
    <rect class="paper" x="45" y="92" width="838" height="363"/>
    <use href="#tread-strips"/>
    <text class="race-number outlined" x="477" y="388" textLength="400" lengthAdjust="spacingAndGlyphs">29</text>
    <polygon class="ink" points="265,408 667,405 692,455 238,455"/>
    <text class="brand-name on-dark" x="470" y="463">K-TRAX</text>
  </g>

  <!-- Row 2 right: black frame, outlined yellow number, yellow badge -->
  <g class="plate plate--ink-frame" transform="translate(1050 622)">
    <rect class="ink" x="0" y="0" width="925" height="484" rx="30"/>
    <rect class="sun" x="45" y="24" width="838" height="62" rx="12"/>
    <use href="#mount-holes" transform="translate(0 15)"/>
    <rect class="paper" x="45" y="92" width="838" height="363"/>
    <use href="#tread-strips"/>
    <text class="race-number outlined" x="477" y="388" textLength="400" lengthAdjust="spacingAndGlyphs">29</text>
    <polygon class="sun outline" points="258,413 662,410 700,476 218,476" stroke-linejoin="round"/>
    <text class="brand-name on-sun" x="460" y="461">K-TRAX</text>
  </g>

  <!-- Row 3 left: black frame, yellow base, black badge -->
  <g class="plate plate--mixed-frame" transform="translate(75 1213)">
    <rect class="ink" x="0" y="0" width="925" height="487" rx="30"/>
    <rect class="sun" x="45" y="24" width="838" height="62" rx="12"/>
    <use href="#mount-holes" transform="translate(0 15)"/>
    <rect class="paper" x="45" y="92" width="838" height="363"/>
    <path class="sun" d="M0,455 H925 V462 Q925,487 895,487 H30 Q0,487 0,462 Z"/>
    <rect class="ink" x="3" y="100" width="48" height="370" rx="14"/>
    <rect class="ink" x="874" y="100" width="48" height="370" rx="14"/>
    <use href="#tread-strips"/>
    <text class="race-number solid" x="477" y="385" textLength="400" lengthAdjust="spacingAndGlyphs">29</text>
    <polygon class="ink" points="265,413 667,411 705,487 223,485"/>
    <text class="brand-name on-dark" x="470" y="466">K-TRAX</text>
  </g>

  <!-- Row 3 right: black frame, yellow base, yellow badge -->
  <g class="plate plate--mixed-frame" transform="translate(1050 1213)">
    <rect class="ink" x="0" y="0" width="925" height="487" rx="30"/>
    <rect class="sun" x="45" y="24" width="838" height="62" rx="12"/>
    <use href="#mount-holes" transform="translate(0 15)"/>
    <rect class="paper" x="45" y="92" width="838" height="363"/>
    <path class="sun" d="M0,455 H925 V462 Q925,487 895,487 H30 Q0,487 0,462 Z"/>
    <rect class="ink" x="3" y="100" width="48" height="370" rx="14"/>
    <rect class="ink" x="874" y="100" width="48" height="370" rx="14"/>
    <use href="#tread-strips"/>
    <text class="race-number solid" x="477" y="385" textLength="400" lengthAdjust="spacingAndGlyphs">29</text>
    <polygon class="sun" points="260,410 665,408 690,456 235,456"/>
    <text class="brand-name on-sun" x="462" y="462">K-TRAX</text>
  </g>
</svg>
</body>
</html>
```